Webpage for co-working space for tech startups

We have an established co-working space in Aalborg Denmark where we have around 30 companies sharing office space. We are starting a new chapter for us and would like to have a new graphical image - new logo and new webpage, but keep the same name. The webpage should be professional, but also "fun", not too serious. We are all about working hard on our companies, but also taking some time off in between and being social and having fun. We are not corporate, but want to project the image that we are serious about what we do.

We currently have a black/red logo (see www.hivelane.dk or test.hivelane.dk), but are interesting in having a new logo design, so colour can be chosen freely. Currently our logo is a big HIVE and a little lane underneath the HIVE. The new logo will be one word "hivelane" with a small logo before or on top.

If we can make a good webpage for this project, then I have a second more simple project which is also a small single page wordpress site which I would also like to have made.

Target Market(s)

tech startups - relatively new companies, typically younger people 20-35 with a tech background - business or programming, preferably both

Industry/Entity Type

HIVE

Logo Text

hivelane

Coding

Coded - Design and coding required

Number of Pages Required

4 page

Font styles to use
Sans Serif

Colors

Designer to choose colors to be used in the design.

Requirements
Must have
• Wordpress CMS.
• Mobile and PC optimized
• 2 languages - English and Danish
• Four sections, could be four pages, or four sections of a single page.
• "Home", "Residents", "Our Working Space", "Our Event Space"
• Footer of page or pages should have contact information.
• "Home" has some information about who we are and what we do
• "Residents" has a list of all our residents - it should be possible to easily add and removed new / old residents - See one example here: http://test.hivelane.dk/en_GB/beboere/ or another example here: http://www.hivelane.dk/beboere/ - one of our colleagues http://copperyard.dk/startups/ or another one of our colleagues http://www.tidalmillhall.dk/residents/
• "Our working space" will have a description of our building, a map of where it is and a bunch of photos which show the different offices, meeting rooms and people working
• "Our events space" will have a description of our event spaces, details of cost + different arrangments of furniture, and lots of photos of events, see here for an example http://www.hivelane.dk/lej-vores-lokaler/
• Our current webpage - www.hivelane.dk was put together very quickly and has not really been optimized. We started a new webpage test.hivelane.dk, but it was never really finished.
• We are looking for a simple webpage, not too much going on. Examples of some of our colleagues in the business http://copperyard.dk/, http://www.tidalmillhall.dk/,
Nice to have
• http://www.tidalmillhall.dk/ is a really good template for us. If we can get something like this, we are happy.

```html
<!DOCTYPE html>
<html lang="en">
<head>
<meta charset="utf-8">
<title>Hivelane – Co-working Space</title>
<link rel="stylesheet" href="https://fonts.googleapis.com/css2?family=Questrial&family=Lato:wght@400;700&display=swap">
<style>
:root{
  --blue:#3ba7dd;
  --blue-dark:#2f95c9;
  --ink:#4a4a4a;
  --muted:#6b6b6b;
  --light:#f1f1f1;
  --footer:#2b2b2d;
  --white:#ffffff;
}
*{box-sizing:border-box;margin:0;padding:0}
html,body{width:1200px;height:3930px;overflow:hidden}
body{font-family:"Lato",sans-serif;color:var(--ink);background:var(--white);position:relative}
section,header,footer{position:absolute;left:0;width:1200px}
.abs{position:absolute}
.heading{font-family:"Questrial",sans-serif;text-transform:uppercase;text-align:center;color:var(--ink);font-size:40px;letter-spacing:1px;font-weight:400}
.rule{position:absolute;left:50%;width:250px;height:2px;background:var(--blue);transform:translateX(-50%)}
.btn{position:absolute;display:flex;align-items:center;justify-content:center;font-size:13px;text-transform:uppercase;letter-spacing:1px;border-radius:3px;font-family:"Lato",sans-serif}
.btn-blue{background:var(--blue);color:var(--white)}
.btn-white{background:var(--white);color:var(--ink)}
.logo{display:flex;align-items:center;gap:8px;color:var(--white);font-family:"Questrial",sans-serif;font-size:26px;letter-spacing:1px}
.logo-mark{width:14px;height:14px;background:var(--blue)}

/* hero */
.hero{top:0;height:663px;background:linear-gradient(180deg,#3b3e42 0%,#5b5f63 35%,#3d3a36 70%,#2b2926 100%)}
.nav{position:absolute;top:8px;left:189px;display:flex;gap:4px}
.nav a{color:var(--white);text-decoration:none;font-size:13px;padding:5px 10px}
.nav a.active{background:var(--blue)}
.lang{position:absolute;top:10px;right:190px;background:#e9e9e9;color:#333;font-size:9px;padding:3px 8px;border-radius:2px}
.hero .logo{position:absolute;top:55px;left:50%;transform:translateX(-50%)}
.hero-kicker{position:absolute;top:250px;left:359px;color:var(--white);font-family:"Questrial",sans-serif;font-size:32px;letter-spacing:1px}
.hero-title{position:absolute;top:292px;left:356px;color:var(--white);font-family:"Questrial",sans-serif;font-size:50px;letter-spacing:1px}
.scroll{position:absolute;top:592px;left:592px;width:16px;height:28px;border:2px solid var(--white);border-radius:8px}
.scroll::after{content:"";position:absolute;left:5px;top:5px;width:2px;height:6px;background:var(--white)}

/* about */
.about{top:663px;height:380px}
.about .heading{position:absolute;top:60px;width:100%}
.about .rule{top:123px}
.about-text{position:absolute;top:152px;left:290px;width:620px;text-align:center;font-size:11.5px;line-height:1.5;color:var(--muted)}
.about-text p+p{margin-top:10px}

/* resident */
.resident{top:1043px;height:406px}
.resident-panel{position:absolute;left:0;top:0;width:608px;height:406px;background:var(--blue);color:var(--white)}
.resident-panel h2{position:absolute;top:42px;left:189px;font-family:"Questrial",sans-serif;font-size:38px;font-weight:400}
.resident-panel .line{position:absolute;top:96px;left:189px;width:345px;height:1px;background:rgba(255,255,255,.7)}
.resident-panel h3{position:absolute;top:128px;left:189px;font-family:"Questrial",sans-serif;font-size:17px;font-weight:400}
.resident-text{position:absolute;top:160px;left:189px;width:340px;font-size:11px;line-height:1.4}
.resident-text p+p{margin-top:10px}
.resident-photo{position:absolute;left:608px;top:0;width:592px;height:406px;background:linear-gradient(180deg,#7da8d6 0%,#a9c4e0 35%,#a54b3d 50%,#8a3c33 68%,#5f7b3a 80%,#4f6a30 100%)}

/* working space */
.working{top:1449px;height:733px}
.working .heading{position:absolute;top:60px;width:100%}
.working .rule{top:123px}
.gallery{position:absolute;top:170px;left:189px;width:820px;height:490px;display:grid;grid-template-columns:1fr 1fr;grid-template-rows:1fr 1fr}
.tile{position:relative}
.tile-a{background:linear-gradient(180deg,#9fb4c8 0%,#b7c4cf 40%,#9b4a3f 58%,#5f7a36 85%,#4c6530 100%)}
.tile-b{background:linear-gradient(180deg,#6f93c4 0%,#9ab4d6 30%,#a6503f 50%,#cfc7bd 70%,#55712f 100%)}
.tile-c{background:radial-gradient(circle at 45% 55%,#a8c79a 0%,#6b8f70 18%,#23406d 40%,#1d3560 100%)}
.tile-d{background:linear-gradient(180deg,#3c3a37 0%,#4a4641 45%,#2e2d2b 100%)}
.tile-d svg{position:absolute;left:50%;top:50%;transform:translate(-50%,-50%)}

/* facilities */
.facilities{top:2182px;height:496px;background:linear-gradient(180deg,#3ea8de 0%,#4aaee0 50%,#39a2d8 100%)}
.facilities .heading{position:absolute;top:50px;width:100%;color:var(--white)}
.facilities .rule{top:113px;background:var(--white)}
.feature{position:absolute;width:260px;color:var(--white)}
.feature-head{display:flex;align-items:center;gap:10px;font-size:11.5px;text-transform:uppercase;letter-spacing:.5px}
.feature p{margin-top:4px;margin-left:0;font-size:11px;line-height:1.35}
.facilities .btn{top:401px;left:511px;width:175px;height:40px;font-size:11px}

/* events */
.events{top:2678px;height:870px}
.events .heading{position:absolute;top:54px;width:100%}
.events .rule{top:117px}
.event-card{position:absolute;top:165px;width:400px;height:463px;background:var(--light)}
.event-photo{height:246px}
.photo-people{background:linear-gradient(135deg,#e8e4de 0%,#c9b9a3 40%,#2f3542 70%,#6a4b3a 100%)}
.photo-glasses{background:linear-gradient(135deg,#d9d3c9 0%,#efece6 45%,#b8a98e 75%,#6f6553 100%)}
.event-body{text-align:center;padding-top:20px}
.event-body h3{font-family:"Questrial",sans-serif;color:var(--blue);font-size:28px;font-weight:400;text-transform:uppercase}
.event-body .sub{font-size:12px;color:var(--ink);margin-top:4px}
.event-body .price{font-size:11px;color:var(--blue);margin-top:6px}
.event-body p{font-size:13px;line-height:1.35;margin:14px auto 0;width:330px;color:var(--ink)}
.note{position:absolute;top:651px;left:189px;font-size:12px;color:var(--ink)}
.note b{color:var(--blue);font-weight:400}
.events .btn{top:710px;left:511px;width:178px;height:42px;font-size:11px}

/* partners */
.partners{top:3548px;height:94px}
.partner{position:absolute;top:0;display:flex;align-items:center;gap:6px;font-family:"Questrial",sans-serif;font-size:16px;color:#1e3a64;text-transform:uppercase}
.partner .dot{width:14px;height:14px;border-radius:50%;background:#1e3a64}

/* footer */
.site-footer{top:3642px;height:288px;background:var(--footer);color:var(--white)}
.site-footer .logo{position:absolute;top:38px;left:50%;transform:translateX(-50%)}
.foot-col{position:absolute;top:110px}
.foot-col h4{font-family:"Questrial",sans-serif;font-size:17px;font-weight:400;text-transform:uppercase;margin-bottom:10px}
.foot-col a{display:block;color:var(--blue);text-decoration:none;font-size:12px;line-height:1.3}
.subscribe{position:absolute;top:140px;left:734px;display:flex}
.subscribe .field{width:220px;height:26px;background:var(--white);color:#999;font-size:11px;padding:6px 8px}
.subscribe .send{width:46px;height:26px;background:var(--blue);display:flex;align-items:center;justify-content:center}
.group-link{position:absolute;top:176px;left:734px;display:flex;align-items:center;gap:6px;font-size:11px;color:var(--blue)}
.group-link .sq{width:14px;height:14px;background:var(--blue)}
.foot-rule{position:absolute;top:220px;left:189px;width:820px;height:1px;background:#555}
.copyright{position:absolute;top:244px;width:100%;text-align:center;font-size:11px;color:#ccc}
</style>
</head>
<body>

<header class="hero" role="img" aria-label="Photo of a bright boardroom with a long conference table, chairs and tall windows">
  <nav class="nav">
    <a class="active">Home</a><a>Residents</a><a>Our Working Space</a><a>Our Event Space</a>
  </nav>
  <div class="lang">ENGLISH ▾</div>
  <div class="logo"><span class="logo-mark"></span>hivelane</div>
  <div class="hero-kicker">HIVE</div>
  <h1 class="hero-title">CO-WORKING SPACE</h1>
  <div class="btn btn-white" style="top:362px;left:435px;width:157px;height:39px">Read More</div>
  <div class="btn btn-blue" style="top:362px;left:610px;width:158px;height:39px">Book a Tour</div>
  <div class="scroll"></div>
</header>

<section class="about">
  <h2 class="heading">About Hive</h2>
  <div class="rule"></div>
  <div class="about-text">
    <p>The corporate community at Hivelane is a community of tech entrepreneurs with global growth ambitions. The vision is to create the best possible conditions for North Jutland entrepreneurs by offering them an environment where they can share knowledge, experience, resources, ideas, motivation and inspiration daily.</p>
    <p>With its 2,200 m2, Hivelane can offer both individual offices, flexspaces, meeting rooms, community rooms and smaller prototype workshops. Common to companies is their global ambitions and scalable potential.</p>
  </div>
  <div class="btn btn-blue" style="top:272px;left:516px;width:157px;height:42px">Read More</div>
</section>

<section class="resident">
  <div class="resident-panel">
    <h2>RESIDENT</h2>
    <div class="line"></div>
    <h3>KERNEN IN HIVELANE</h3>
    <div class="resident-text">
      <p>At Hivelane, we do not call the companies at the castle for renters - they are so much more than that. They are inhabitants. These are the ones that help create the right atmosphere. They all form equal to the community. They all have something unique to contribute with and although everyone is doing something widely different, residents have their global ambitions and scalable potential in common.</p>
      <p>Learn more about what we offer residents.</p>
    </div>
    <div class="btn btn-white" style="top:312px;left:189px;width:157px;height:42px;font-size:11px">Learn More</div>
  </div>
  <div class="resident-photo" role="img" aria-label="Photo of the red half-timbered manor building on a green lawn under blue sky"></div>
</section>

<section class="working">
  <h2 class="heading">Our Working Space</h2>
  <div class="rule"></div>
  <div class="gallery">
    <div class="tile tile-a" role="img" aria-label="Photo of the half-timbered building behind a large tree"></div>
    <div class="tile tile-b" role="img" aria-label="Photo of the courtyard wings of the half-timbered building"></div>
    <div class="tile tile-c" role="img" aria-label="Site plan of the building grounds on a dark blue background"></div>
    <div class="tile tile-d" role="img" aria-label="Darkened photo of the building facade with an expand icon">
      <svg width="36" height="36" viewBox="0 0 36 36" fill="none" stroke="#fff" stroke-width="3">
        <path d="M2 12V2h10M24 2h10v10M34 24v10H24M12 34H2V24"/>
      </svg>
    </div>
  </div>
</section>

<section class="facilities">
  <h2 class="heading">Work Space Faclities</h2>
  <div class="rule"></div>

  <div class="feature" style="top:158px;left:189px">
    <div class="feature-head"><svg width="34" height="24" viewBox="0 0 34 24" fill="none" stroke="#fff" stroke-width="2"><path d="M2 9a22 22 0 0 1 30 0M7 14a15 15 0 0 1 20 0M12 19a8 8 0 0 1 10 0"/><circle cx="17" cy="22" r="1.5" fill="#fff"/></svg>Highspeed Internet</div>
    <p>Lorem Ipsum is simply dummy text of<br>the printing and typesetting industry.</p>
  </div>
  <div class="feature" style="top:158px;left:506px">
    <div class="feature-head"><svg width="30" height="26" viewBox="0 0 30 26" fill="none" stroke="#fff" stroke-width="2"><path d="M3 10h18v7a7 7 0 0 1-7 7h-4a7 7 0 0 1-7-7zM21 12h3a3 3 0 0 1 0 6h-3M10 2v5M15 2v5"/></svg>Free Coffe Everyday</div>
    <p>Lorem Ipsum is simply dummy text of<br>the printing and typesetting industry.</p>
  </div>
  <div class="feature" style="top:158px;left:812px">
    <div class="feature-head"><svg width="34" height="24" viewBox="0 0 34 24" fill="none" stroke="#fff" stroke-width="2"><path d="M9 5h16a7 7 0 0 1 7 8l-1 6a3 3 0 0 1-5 1l-4-4h-10l-4 4a3 3 0 0 1-5-1l-1-6a7 7 0 0 1 7-8zM9 10v5M6.5 12.5h5"/><circle cx="24" cy="11" r="1.2" fill="#fff"/><circle cx="27" cy="14" r="1.2" fill="#fff"/></svg>Game Station</div>
    <p>Lorem Ipsum is simply dummy text of<br>the printing and typesetting industry.</p>
  </div>

  <div class="feature" style="top:280px;left:189px">
    <div class="feature-head"><svg width="34" height="26" viewBox="0 0 34 26" fill="none" stroke="#fff" stroke-width="2"><path d="M2 3h18v12H9l-5 4v-4H2zM24 9h8v11h-2v4l-5-4h-9v-3"/></svg>Meeting Room</div>
    <p>Lorem Ipsum is simply dummy text of<br>the printing and typesetting industry.</p>
  </div>
  <div class="feature" style="top:280px;left:506px">
    <div class="feature-head"><svg width="30" height="26" viewBox="0 0 30 26" fill="none" stroke="#fff" stroke-width="2"><rect x="2" y="2" width="26" height="16"/><path d="M15 18v5M9 24h12M9 10l4 3 7-6"/></svg>Conference Room</div>
    <p>Lorem Ipsum is simply dummy text of<br>the printing and typesetting industry.</p>
  </div>
  <div class="feature" style="top:280px;left:812px">
    <div class="feature-head"><svg width="34" height="26" viewBox="0 0 34 26" fill="none" stroke="#fff" stroke-width="2"><rect x="2" y="2" width="30" height="22"/><path d="M9.5 2v22M17 2v22M24.5 2v22M2 8h30"/></svg>Dedicated Lockers</div>
    <p>Lorem Ipsum is simply dummy text of<br>the printing and typesetting industry.</p>
  </div>

  <div class="btn btn-white">Explore All Facilities</div>
</section>

<section class="events">
  <h2 class="heading">Our Event Space</h2>
  <div class="rule"></div>

  <article class="event-card" style="left:189px">
    <div class="event-photo photo-people" role="img" aria-label="Photo of guests talking at a lounge event"></div>
    <div class="event-body">
      <h3>Day Event</h3>
      <div class="sub">Lounge Area</div>
      <div class="price">Rent Of The Lounge: 3000,- Ex Moms</div>
      <p>Morning meeting for 30 guests. We serve you breakfast, water, organic tea and coffee from our in-house barista to get you on your feet.</p>
    </div>
  </article>

  <article class="event-card" style="left:610px">
    <div class="event-photo photo-glasses" role="img" aria-label="Photo of a bottle and glasses set out on a table for a reception"></div>
    <div class="event-body">
      <h3>Standing Reception</h3>
      <div class="sub">Canteen Area</div>
      <div class="price">Rent Of The Canteen: 5000,- Ex Moms</div>
      <p>When you have something to celebrate. For 50 guests. Light fingerfood, wine, and non-alcoholic refreshments are included.</p>
    </div>
  </article>

  <div class="note"><b>NOTE :</b> If you need to rent the premises for a shorter period or in the evening hours, the hourly rate is 475,- ex VAT.</div>
  <div class="btn btn-blue">View More Events</div>
</section>

<section class="partners">
  <div class="partner" style="left:189px"><span class="dot"></span>Northwall</div>
  <div class="partner" style="left:430px;color:#c0392b">Ravnsted</div>
  <div class="partner" style="left:678px;font-size:13px">Fjordline Bank</div>
  <div class="partner" style="left:918px;font-size:12px;color:#222">Aksel Holm</div>
</section>

<footer class="site-footer">
  <div class="logo"><span class="logo-mark"></span>hivelane</div>

  <div class="foot-col" style="left:189px"><h4>About</h4><a>About Us</a><a>Contact Us</a><a>F.A.Q.</a><a>Privacy</a></div>
  <div class="foot-col" style="left:388px"><h4>Space</h4><a>Resident</a><a>Working Spaces</a><a>Event Spaces</a></div>
  <div class="foot-col" style="left:590px"><h4>Legal</h4><a>Privacy</a><a>Terms</a><a>Advertise</a><a>Sponsors</a></div>
  <div class="foot-col" style="left:734px"><h4>Subscribe</h4></div>

  <div class="subscribe">
    <div class="field">E-Mail Address</div>
    <div class="send"><svg width="16" height="14" viewBox="0 0 16 14"><path d="M1 7L15 1 11 13 8 8z" fill="#fff"/></svg></div>
  </div>
  <div class="group-link"><span class="sq"></span>community.hivelane.dk/aalborg</div>

  <div class="foot-rule"></div>
  <div class="copyright">© Copyright 2018 . hivelane.All Right Reserved</div>
</footer>

</body>
</html>
```